Professional Corporate Business Card and Stationery Design for Freight Trucking Transportation Co.
Peter R. Malloy General Manager
Professional Corporate Business Card and Stationery Design for Freight Trucking Transportation Co. - Transportation
Creative Brief
Professional
Peter R. Malloy
V.P. of Operations / General Manager
7-48213 Upper Greyling Ridge Road Abbotsford, B.C. V2K4N7 Canada
HarrowTrans@pelvane.ca
This design project is for Business Cards and Business Stationey Harrow Transportation and Logistics Ltd. is a professional freight truck transport carrier based out of British Columbia, Canada. We provide highly crafted cargo delivery platforms to premier shippers of commodities throughout the five border Provinces of Canada and the Lower 48 United States of America. We are a "For-Hire" Motor Carrier which hauls shipper commodities from points within Canada to points within Canada and to points in the USA. We also transport freight from the United States into points within Canada. Threfore, we pride ourselves on superior performance and service, second to none in trucking freight industry. The above link will take you to what we feel is a example set of very highly crafted, upscale imagery designs created by artists on this very site and exemplifies the grit and character of true, quality Business card and Stationery designs, representation of the values of business professionalism we stand for and wish to convey in our stationery and other designs. Are you challenged enough to join in the fray and craft a unique design which can stand on par with those on this link? Today is April 25, 2014 - The challenge is to wow not only Harrow, but yourselves and your peers... ??
Harrow Harrow

```html
<!DOCTYPE html>
<html lang="en">
<head>
<meta charset="utf-8">
<title>Harrow Transportation and Logistics Ltd. – Business Card</title>
<link rel="stylesheet" href="https://fonts.googleapis.com/css2?family=Open+Sans:wght@400;600;700&display=swap">
<style>
  :root {
    --card-white: #f7f7f7;
    --ink-dark: #2b2b2b;
    --ink-mid: #3a3a3a;
    --brand-red: #e3101f;
    --band-black: #1c1c1c;
    --page-bg: #d9d9d9;
  }
  * { margin: 0; padding: 0; box-sizing: border-box; }
  html, body { width: 1200px; height: 816px; overflow: hidden; background: var(--page-bg); }
  .business-card {
    position: relative;
    width: 1200px;
    height: 816px;
    background: var(--card-white);
    overflow: hidden;
    font-family: "Open Sans", Arial, sans-serif;
  }
  .card-shapes { position: absolute; inset: 0; }
  .holder {
    position: absolute;
    left: 70px;
    top: 270px;
  }
  .holder-name {
    font-size: 44px;
    font-weight: 600;
    color: var(--ink-dark);
    letter-spacing: 1px;
    text-transform: uppercase;
    line-height: 1.1;
  }
  .holder-title {
    font-size: 30px;
    color: var(--brand-red);
    margin-top: 4px;
  }
  .contact-list {
    position: absolute;
    left: 70px;
    top: 440px;
    list-style: none;
    font-size: 25px;
    color: var(--ink-mid);
    font-weight: 600;
    line-height: 1.3;
  }
  .contact-list li { display: flex; align-items: flex-start; gap: 16px; margin-bottom: 4px; }
  .contact-list svg { width: 22px; height: 22px; flex: none; margin-top: 6px; fill: var(--brand-red); }
  .address { max-width: 300px; }
  .brand-mark {
    position: absolute;
    right: 80px;
    top: 300px;
    display: flex;
    align-items: center;
    gap: 16px;
  }
  .brand-dot { width: 52px; height: 52px; border-radius: 50%; background: var(--brand-red); }
  .brand-name {
    font-size: 54px;
    font-weight: 700;
    color: var(--brand-red);
    text-transform: uppercase;
    letter-spacing: 1px;
  }
  .website {
    position: absolute;
    left: 660px;
    top: 418px;
    width: 500px;
    font-size: 36px;
    color: #ffffff;
    font-weight: 400;
    text-align: center;
  }
</style>
</head>
<body>
<div class="business-card">
  <svg class="card-shapes" width="1200" height="816" viewBox="0 0 1200 816" aria-hidden="true">
    <path d="M0 700 C 250 700 460 690 560 600 L 640 520 L 1200 520 L 1200 816 L 0 816 Z" fill="var(--band-black)"/>
    <path d="M600 395 L 1200 395 L 1200 500 L 600 500 A 52 52 0 0 1 600 395 Z" fill="var(--brand-red)"/>
  </svg>

  <div class="holder">
    <div class="holder-name">Martin Selwyn</div>
    <div class="holder-title">Managing Director</div>
  </div>

  <ul class="contact-list">
    <li>
      <svg viewBox="0 0 24 24"><path d="M12 2a7 7 0 0 0-7 7c0 5 7 13 7 13s7-8 7-13a7 7 0 0 0-7-7zm0 9.5a2.5 2.5 0 1 1 0-5 2.5 2.5 0 0 1 0 5z"/></svg>
      <span class="address">27-4th floor, Kestrel Park Road ABT</span>
    </li>
    <li>
      <svg viewBox="0 0 24 24"><path d="M6.6 10.8a15 15 0 0 0 6.6 6.6l2.2-2.2a1 1 0 0 1 1-.25 11.4 11.4 0 0 0 3.6.57 1 1 0 0 1 1 1V20a1 1 0 0 1-1 1A17 17 0 0 1 3 4a1 1 0 0 1 1-1h3.5a1 1 0 0 1 1 1c0 1.25.2 2.45.57 3.57a1 1 0 0 1-.25 1z"/></svg>
      <span>014 552 7310</span>
    </li>
    <li>
      <svg viewBox="0 0 24 24"><path d="M4 6h16v12H4z M7 3h10v3H7z M8 10h8v2H8z"/></svg>
      <span>014 552 7310</span>
    </li>
    <li>
      <svg viewBox="0 0 24 24"><path d="M3 5h18v14H3z M3 5l9 7 9-7" stroke="#fff" stroke-width="1.5"/></svg>
      <span>m.selwyn@pelvane.ca</span>
    </li>
  </ul>

  <div class="brand-mark">
    <div class="brand-dot"></div>
    <div class="brand-name">Harrow</div>
  </div>

  <div class="website">www.harrowfreight.ca</div>
</div>
</body>
</html>
```